Heronbay Poolworks, LLC Business Card

We have a well designed logo that we need incorporated into a professional and unique business card. Heronbay Poolworks provides professional swimming pool management. From openings to closings, inspections, chemicals, maintenance, lifeguard, safety audits, learn to swim lessons, etc. etc.
Different colors of blue are ideal. The final design should include water, clean water (very clean crystal clear water), and perhaps safety.
content/design ideas:
Milo Fenster, President - Owner
milo@heronbaypoolworks.example
office: 555-412-8391
cell: 555-630-2175
www.heronbaypoolworks.example
"Every Swim: Safe, Fresh, Crystal Clear"
Target Market(s)
Our customers are mostly home owners associations and property management companies. Adults, aged 25 to 55. Mostly with young children.
Industry/Entity Type
Safety
Look and feel

```html
<!DOCTYPE html>
<html lang="en">
<head>
<meta charset="utf-8">
<title>Heronbay Poolworks, LLC – Business Card</title>
<link rel="stylesheet" href="https://fonts.googleapis.com/css2?family=Open+Sans:wght@400;600;700&display=swap">
<style>
  :root {
    --page-bg: #e9edf1;
    --card-white: #ffffff;
    --brand-blue: #1a5fb4;
    --brand-blue-deep: #1b4f9c;
    --ink: #1f1f1f;
    --ink-soft: #444444;
    --water-deep: #1f66b8;
    --water-mid: #3a8fd8;
    --water-light: #6fc3ee;
    --pool-light: #8fd6f2;
    --pool-mid: #4fb3e6;
    --pool-deep: #2a86c8;
    --strip: rgba(255, 255, 255, 0.55);
  }
  * { box-sizing: border-box; margin: 0; padding: 0; }
  html, body {
    width: 1200px; height: 1000px; overflow: hidden;
    background: var(--page-bg);
    font-family: "Open Sans", Arial, sans-serif;
  }
  .stage {
    width: 1200px; height: 1000px;
    display: flex; flex-direction: column; align-items: center; justify-content: center;
    gap: 60px;
  }
  .card {
    position: relative;
    width: 560px; height: 320px;
    overflow: hidden;
    box-shadow: 0 6px 18px rgba(0, 0, 0, 0.18);
  }

  /* Front */
  .card--front { background: var(--card-white); }
  .contact {
    position: absolute; left: 44px; top: 92px;
    color: var(--ink);
  }
  .contact__name { font-size: 21px; font-weight: 700; color: var(--brand-blue); }
  .contact__role { font-size: 14px; color: var(--ink-soft); margin-top: 2px; }
  .contact__lines { margin-top: 16px; font-size: 14.5px; line-height: 21px; }
  .company {
    position: absolute; right: 28px; top: 70px; width: 240px;
    text-align: center;
  }
  .company__mark {
    display: flex; align-items: center; justify-content: center; gap: 8px;
  }
  .company__dot {
    width: 16px; height: 16px; border-radius: 50%;
    background: var(--brand-blue);
  }
  .company__name {
    font-size: 20px; font-weight: 700; color: var(--brand-blue); line-height: 1.1;
  }
  .company__address {
    margin-top: 26px; font-size: 12px; line-height: 19px; color: var(--ink);
  }
  .tagline-band {
    position: absolute; left: 0; right: 0; bottom: 0; height: 74px;
    background: linear-gradient(180deg, var(--water-deep) 0%, var(--water-mid) 55%, var(--water-light) 100%);
  }
  .tagline-band__text {
    position: absolute; left: 0; right: 0; bottom: 14px;
    text-align: center; color: #ffffff; font-size: 19px;
  }

  /* Back */
  .pool-scene {
    position: absolute; inset: 0;
    background: linear-gradient(160deg, var(--pool-light) 0%, var(--pool-mid) 50%, var(--pool-deep) 100%);
  }
  .back-strip {
    position: absolute; left: 0; right: 0; top: 150px; height: 96px;
    background: var(--strip);
  }
  .back-brand {
    position: absolute; right: 36px; top: 96px;
    display: flex; align-items: center; gap: 10px;
  }
  .back-brand .company__dot { width: 20px; height: 20px; }
  .back-brand .company__name { font-size: 26px; }
  .back-tagline {
    position: absolute; right: 36px; top: 184px;
    font-size: 24px; font-weight: 700;
    color: var(--brand-blue-deep);
  }
</style>
</head>
<body>
  <main class="stage">
    <section class="card card--front" aria-label="Business card front">
      <div class="contact">
        <p class="contact__name">Milo Fenster</p>
        <p class="contact__role">President / Owner</p>
        <p class="contact__lines">
          milo@heronbaypoolworks.example<br>
          office: 555-412-8391<br>
          cell: 555-630-2175
        </p>
      </div>
      <div class="company">
        <div class="company__mark">
          <span class="company__dot"></span>
          <span class="company__name">Heronbay Poolworks</span>
        </div>
        <p class="company__address">
          2240 Marsh Hollow Rd.<br>
          Suite 410 #18, Brenton, NC 27000<br>
          www.heronbaypoolworks.example
        </p>
      </div>
      <div class="tagline-band" role="img" aria-label="Clear blue rippling pool water"></div>
      <p class="tagline-band__text">"Every Swim: Safe, Fresh, Crystal Clear"</p>
    </section>

    <section class="card card--back" aria-label="Business card back">
      <div class="pool-scene" role="img" aria-label="Photo of a swimming pool with lane ropes, a diving board and a steel ladder"></div>
      <div class="back-strip"></div>
      <div class="back-brand">
        <span class="company__dot"></span>
        <span class="company__name">Heronbay Poolworks</span>
      </div>
      <p class="back-tagline">Every Swim: Safe, Fresh, Crystal Clear</p>
    </section>
  </main>
</body>
</html>
```